Business Card Re-Design for a Lighting Designer

I would like my business card re-designed. It is currently high gloss and they scratch too easily. I don not think the current design lends itself well to a matte finish. I have included the current design for reference along with our company logo.
Check out our website for current branding.
http://www.brambleorchidstudio.example

Updates
Some of the top contenders are muslim and it is a holiday for them. I do not want to discriminate and would expect the same courtesy for holidays we celebrate.
Target Market(s)
Interior Designers, Architects
Contact Information for Business Card
Logo - Name, Title, Address, Telephone Number and Extension, Email
Font styles to use
Requirements
Must have
- All the information listed on the current business card. If you use Red, it needs to be the red from our logo.
Nice to have
- Vertical and Horizontal Designs will be entertained.
Should not have
- Requirements for a glossy finish...should not look too corporate since we are a design firm.

```html
<!DOCTYPE html>
<html lang="en">
<head>
<meta charset="utf-8">
<title>Bramble Orchid Studio — Business Card</title>
<link href="https://fonts.googleapis.com/css2?family=Lato:wght@400;700;900&family=Roboto+Condensed:wght@300;400&display=swap" rel="stylesheet">
<style>
  :root {
    --backdrop: #3a3633;
    --paper: #f1f1ef;
    --ink: #2b2b2b;
    --ink-soft: #4a4a4a;
    --brand-red: #9e1418;
    --brand-red-deep: #860f12;
    --emboss: #7a0c0f;
  }
  * { box-sizing: border-box; margin: 0; padding: 0; }
  html, body { width: 1200px; height: 672px; overflow: hidden; }
  body {
    background: var(--backdrop);
    display: flex;
    align-items: center;
    justify-content: center;
    gap: 56px;
    font-family: "Lato", Arial, sans-serif;
  }
  .card {
    width: 330px;
    height: 576px;
    position: relative;
  }
  .card--front {
    background: var(--paper);
    color: var(--ink);
    padding: 48px 36px 40px 40px;
    display: flex;
    flex-direction: column;
  }
  .card--back {
    background: var(--brand-red);
    display: flex;
    flex-direction: column;
    align-items: center;
    justify-content: center;
  }
  .brand {
    display: flex;
    flex-direction: column;
    align-items: flex-start;
    gap: 10px;
  }
  .brand__square {
    width: 58px;
    height: 58px;
    background: var(--brand-red);
  }
  .brand__name {
    font-family: "Roboto Condensed", Arial, sans-serif;
    font-weight: 400;
    font-size: 27px;
    line-height: 1.02;
    letter-spacing: -0.5px;
    text-transform: uppercase;
    color: var(--ink);
  }
  .person { margin-top: 96px; }
  .person__name {
    font-family: "Roboto Condensed", Arial, sans-serif;
    font-weight: 400;
    font-size: 30px;
    letter-spacing: -0.6px;
    text-transform: uppercase;
  }
  .person__title {
    margin-top: 4px;
    font-weight: 900;
    font-size: 14px;
    letter-spacing: 1px;
    color: var(--brand-red);
  }
  .contact {
    list-style: none;
    margin-top: 40px;
    display: flex;
    flex-direction: column;
    gap: 10px;
    font-size: 13.5px;
    color: var(--ink);
  }
  .contact__item { display: flex; align-items: center; gap: 12px; }
  .contact__item--web { font-weight: 700; }
  .contact__icon { width: 20px; height: 20px; flex: none; }
  .rule {
    border: 0;
    height: 1.5px;
    background: var(--brand-red);
    margin-top: 26px;
  }
  .address {
    font-style: normal;
    margin-top: 26px;
    font-family: "Roboto Condensed", Arial, sans-serif;
    font-size: 15px;
    line-height: 1.3;
    color: var(--ink-soft);
  }
  .emboss {
    display: flex;
    flex-direction: column;
    align-items: flex-start;
    gap: 12px;
    color: var(--emboss);
  }
  .emboss__square {
    width: 92px;
    height: 92px;
    border: 1.5px solid var(--emboss);
  }
  .emboss__name {
    font-family: "Roboto Condensed", Arial, sans-serif;
    font-weight: 400;
    font-size: 38px;
    line-height: 1;
    letter-spacing: -0.8px;
    text-transform: uppercase;
  }
  .emboss__tagline {
    border-top: 1.5px solid var(--emboss);
    padding-top: 4px;
    font-family: "Roboto Condensed", Arial, sans-serif;
    font-size: 13px;
    letter-spacing: 1px;
    text-transform: uppercase;
  }
</style>
</head>
<body>
  <section class="card card--front">
    <div class="brand">
      <div class="brand__square"></div>
      <div class="brand__name">Bramble<br>Orchid Studio</div>
    </div>

    <div class="person">
      <h1 class="person__name">Maren Holloway</h1>
      <p class="person__title">PRINCIPAL</p>
    </div>

    <ul class="contact">
      <li class="contact__item">
        <svg class="contact__icon" viewBox="0 0 20 20" aria-hidden="true">
          <circle cx="10" cy="10" r="8.5" fill="none" stroke="var(--brand-red)" stroke-width="1.4"/>
          <path d="M7 5.5l1.6 2-1 1.2c.6 1.3 1.5 2.2 2.7 2.8l1.2-1 2 1.6-1 1.6c-3.4-.4-6.3-3.3-6.6-6.7z" fill="var(--brand-red)"/>
        </svg>
        <span>555.014.2290 x1</span>
      </li>
      <li class="contact__item">
        <svg class="contact__icon" viewBox="0 0 20 20" aria-hidden="true">
          <circle cx="10" cy="10" r="8.5" fill="none" stroke="var(--brand-red)" stroke-width="1.4"/>
          <rect x="5.5" y="6.8" width="9" height="6.4" fill="var(--brand-red)"/>
          <path d="M5.5 6.8l4.5 3.6 4.5-3.6" fill="none" stroke="var(--paper)" stroke-width="1"/>
        </svg>
        <span>maren@brambleorchidstudio.example</span>
      </li>
      <li class="contact__item contact__item--web">
        <svg class="contact__icon" viewBox="0 0 20 20" aria-hidden="true">
          <circle cx="10" cy="10" r="8.5" fill="none" stroke="var(--brand-red)" stroke-width="1.4"/>
          <rect x="5.5" y="6" width="9" height="6" fill="none" stroke="var(--brand-red)" stroke-width="1.2"/>
          <path d="M8 14h4M10 12v2" stroke="var(--brand-red)" stroke-width="1.2"/>
        </svg>
        <span>www.brambleorchidstudio.example</span>
      </li>
    </ul>

    <hr class="rule">

    <address class="address">
      412 Fernbrook Lane, Suite 210<br>
      Marlow, Oregon 97035 USA
    </address>
  </section>

  <section class="card card--back">
    <div class="emboss">
      <div class="emboss__square"></div>
      <div class="emboss__name">Bramble<br>Orchid Studio</div>
      <div class="emboss__tagline">Lighting for Architecture</div>
    </div>
  </section>
</body>
</html>
```